Business Card & Stationery
It must INSTANTLY show u exactly what the business is
Project: Business Card & Stationery
Business Card & Stationery -
Creative Brief
Professional
Gavin Pellworth
Managing Director
PO Box 482 Fernhollow Vic 3159
gavin@brindlecheckfix.com.au
www.brindlecheckfix.com.au
Cert No. QRBX 392
Testing & Tagging to ASNZS 3760 Microwave Oven Leakage Testing Safety Switch Testing (RCD) Jobguard Compliance
Gavin Pellworth Managing Director Tel: 0427 315 682 Brindle Check & Fix Pty Ltd PO Box 482 Fernhollow Vic 3159 Email: gavin@brindlecheckfix.com.au Website: www.brindlecheckfix.com.au

```html
<!DOCTYPE html>
<html lang="en">
<head>
<meta charset="utf-8">
<title>Brindle Check &amp; Fix – Business Card</title>
<link rel="stylesheet" href="https://fonts.googleapis.com/css2?family=Open+Sans:wght@400;600;700;800&display=swap">
<style>
  :root {
    --backdrop: #2e2e2e;
    --card: #ffffff;
    --orange: #f47b20;
    --orange-deep: #e2601a;
    --ink: #2b2b2b;
    --ink-soft: #555555;
    --rule: #c9c9c9;
  }
  * { margin: 0; padding: 0; box-sizing: border-box; }
  html, body {
    width: 1200px; height: 780px; overflow: hidden;
    background: var(--backdrop);
    font-family: "Open Sans", Arial, sans-serif;
  }
  .canvas {
    position: relative; width: 1200px; height: 780px;
    display: flex; align-items: center; justify-content: center;
  }
  .business-card {
    position: relative; width: 960px; height: 580px;
    background: var(--card); border-radius: 34px; overflow: hidden;
  }
  .edge-tab {
    position: absolute; width: 14px; background: var(--orange);
    background: linear-gradient(180deg, var(--orange), var(--orange-deep));
  }
  .edge-tab--left { left: 0; top: 360px; height: 130px; border-radius: 0 7px 7px 0; }
  .edge-tab--right { right: 0; top: 250px; height: 130px; border-radius: 7px 0 0 7px; }

  .brand {
    position: absolute; top: 80px; left: 0; right: 0;
    display: flex; align-items: center; justify-content: center; gap: 22px;
  }
  .brand-mark { width: 40px; height: 40px; border-radius: 50%; background: var(--orange); }
  .brand-name {
    font-weight: 800; font-size: 66px; letter-spacing: 1px;
    text-transform: uppercase; color: var(--orange); line-height: 1;
  }

  .divider {
    position: absolute; left: 478px; top: 270px; width: 2px; height: 210px;
    background: var(--rule);
  }
  .person {
    position: absolute; right: 505px; top: 318px; text-align: right;
  }
  .person-name { font-weight: 700; font-size: 30px; color: var(--orange); }
  .person-role { font-weight: 700; font-size: 21px; color: var(--ink); margin-top: 2px; }
  .licence {
    position: absolute; right: 505px; top: 448px;
    font-size: 19px; color: var(--ink-soft);
  }

  .contact { position: absolute; left: 505px; top: 272px; color: var(--ink-soft); }
  .address { font-size: 19px; line-height: 28px; }
  .contact-list { list-style: none; margin-top: 40px; }
  .contact-list li {
    display: flex; align-items: center; gap: 12px;
    font-size: 19px; line-height: 34px;
  }
  .contact-icon { width: 20px; height: 20px; flex: none; }
</style>
</head>
<body>
<main class="canvas">
  <section class="business-card">
    <span class="edge-tab edge-tab--left"></span>
    <span class="edge-tab edge-tab--right"></span>

    <header class="brand">
      <span class="brand-mark"></span>
      <span class="brand-name">Brindle Check &amp; Fix</span>
    </header>

    <div class="person">
      <p class="person-name">Gavin Pellworth</p>
      <p class="person-role">Managing Director</p>
    </div>
    <p class="licence">License No. Cert No. QRBX 392</p>

    <span class="divider"></span>

    <div class="contact">
      <p class="address">PO Box 482<br>Fernhollow Vic 3159</p>
      <ul class="contact-list">
        <li>
          <svg class="contact-icon" viewBox="0 0 24 24" aria-hidden="true">
            <path fill="#f47b20" d="M6.6 10.8a15.1 15.1 0 0 0 6.6 6.6l2.2-2.2c.3-.3.7-.4 1-.2 1.1.4 2.3.6 3.6.6.6 0 1 .4 1 1V20c0 .6-.4 1-1 1A17 17 0 0 1 3 4c0-.6.4-1 1-1h3.5c.6 0 1 .4 1 1 0 1.3.2 2.5.6 3.6.1.3 0 .7-.2 1z"/>
          </svg>
          <span>0427 315 682</span>
        </li>
        <li>
          <svg class="contact-icon" viewBox="0 0 24 24" aria-hidden="true">
            <rect x="2" y="5" width="20" height="14" rx="2" fill="#f47b20"/>
            <path d="M3 6.5l9 6.5 9-6.5" fill="none" stroke="#fff" stroke-width="1.8"/>
          </svg>
          <span>gavin@brindlecheckfix.com.au</span>
        </li>
        <li>
          <svg class="contact-icon" viewBox="0 0 24 24" aria-hidden="true">
            <circle cx="12" cy="12" r="10" fill="#f8b27a"/>
            <path d="M2 12h20M12 2c3 3 3 17 0 20M12 2c-3 3-3 17 0 20" fill="none" stroke="#fff" stroke-width="1.4"/>
          </svg>
          <span>www.brindlecheckfix.com.au</span>
        </li>
      </ul>
    </div>
  </section>
</main>
</body>
</html>
```